Brightmoor Signal needs a Business Card

Designers!
More often than not, people want a cheap business card and often argue "I only want 100, not 500" - Years ago I worked in print and always wanted a client to ask for something that challenged me and would be great for my portfolio.

Years have past, and I dont have the time to do it myself so I'd love to see what everyone can offer.

Reason: Hey Guys, The designs are looking good but i've extended it a few more days as I wont be near a laptop and i'm trying to provide everyone feedback - Sorry!

Target Market(s)

Key decision makers, Potential Clients, Networking events and opportunities.

Industry/Entity Type

Business

Requirements
Must have
• Typography is very important. The type of paper is important.
The print, the shape. The creativity.
I'm very inspired by the below link
http://www.palevantro.com/blog/business-card-design/

Nice to have
• Stencelled cutouts. Embossing, nice typography.
I'd like the business card to be a conversation piece itself.

Attached is an image of business cards i've had in the past.
Additionally, some logos i've recently had designed by Quillmarsh.

```html
<!DOCTYPE html>
<html lang="en">
<head>
<meta charset="utf-8">
<title>Brightmoor Signal – Business Cards</title>
<link href="https://fonts.googleapis.com/css2?family=Open+Sans:wght@300;400&display=swap" rel="stylesheet">
<style>
  :root {
    --backdrop: #d9d8d6;
    --navy: #0b2c63;
    --steel: #1d4d85;
    --slate: #5f86ad;
    --ice: #e3eef3;
    --sky: #9cc9da;
    --lime: #8dc63f;
    --paper: #ffffff;
    --card-shadow: 0 14px 22px rgba(0,0,0,.35);
  }
  * { margin: 0; padding: 0; box-sizing: border-box; }
  html, body { width: 1200px; height: 886px; overflow: hidden; }
  body {
    background: var(--backdrop);
    font-family: "Open Sans", Arial, sans-serif;
    position: relative;
  }
  .card {
    position: absolute;
    width: 380px;
    height: 236px;
    border-radius: 20px;
    overflow: hidden;
    box-shadow: var(--card-shadow);
  }
  .card-finish { position: absolute; inset: 0; }

  .card--front-light { left: 60px; top: 190px; background: var(--paper); }
  .card--front-light .card-finish {
    background: linear-gradient(90deg, var(--sky) 0%, var(--ice) 30%, var(--paper) 55%);
  }
  .card--front-dark { left: 480px; top: 150px; background: var(--navy); }
  .card--back { left: 700px; top: 460px; background: var(--navy); }
  .card--front-dark .card-finish,
  .card--back .card-finish {
    background:
      radial-gradient(circle at 100% 100%, rgba(141,198,63,.55) 0%, rgba(141,198,63,0) 38%),
      linear-gradient(100deg, var(--slate) 0%, var(--steel) 22%, var(--navy) 45%);
  }

  .wordmark {
    position: absolute;
    font-weight: 300;
    text-transform: uppercase;
    line-height: 1;
  }
  .wordmark__main { display: block; font-size: 34px; letter-spacing: -1px; }
  .wordmark__sub { display: block; font-size: 13px; letter-spacing: 6px; margin-top: 4px; padding-left: 60px; }
  .mark-square { position: absolute; width: 30px; height: 30px; }
  .rule { position: absolute; height: 1px; }
  .web {
    position: absolute;
    font-size: 14px;
    letter-spacing: 4.5px;
    color: var(--lime);
    font-weight: 400;
  }

  .card--front-light .mark-square { left: 92px; top: 90px; background: var(--navy); }
  .card--front-light .wordmark { left: 132px; top: 84px; color: var(--navy); }
  .card--front-light .rule { left: 92px; right: 18px; top: 138px; background: var(--navy); }
  .card--front-light .web { left: 92px; top: 146px; }

  .card--front-dark .mark-square { left: 78px; top: 84px; background: var(--paper); }
  .card--front-dark .wordmark { left: 118px; top: 78px; color: var(--paper); }
  .card--front-dark .rule { left: 78px; right: 30px; top: 132px; background: rgba(255,255,255,.6); }
  .card--front-dark .web { left: 78px; top: 140px; }

  .card--back .mark-square { right: 176px; top: 32px; width: 22px; height: 22px; background: var(--paper); }
  .card--back .wordmark { right: 22px; top: 30px; color: var(--paper); }
  .card--back .wordmark__main { font-size: 22px; }
  .card--back .web { right: 22px; top: 62px; font-size: 9px; letter-spacing: 2.5px; }
  .contact { position: absolute; left: 150px; top: 86px; color: var(--paper); }
  .contact__name { font-size: 22px; font-weight: 400; margin-bottom: 6px; }
  .contact__line { font-size: 10px; font-weight: 400; line-height: 1.55; }
</style>
</head>
<body>

  <section class="card card--front-light" aria-label="Card front, light">
    <div class="card-finish" role="img" aria-label="Decorative pale blue pattern area"></div>
    <span class="mark-square"></span>
    <div class="wordmark"><span class="wordmark__main">Brightmoor</span><span class="wordmark__sub">Signal</span></div>
    <span class="rule"></span>
    <p class="web">brightmoorsignal.com.au</p>
  </section>

  <section class="card card--front-dark" aria-label="Card front, dark">
    <div class="card-finish" role="img" aria-label="Decorative blue and green pattern area"></div>
    <span class="mark-square"></span>
    <div class="wordmark"><span class="wordmark__main">Brightmoor</span><span class="wordmark__sub">Signal</span></div>
    <span class="rule"></span>
    <p class="web">brightmoorsignal.com.au</p>
  </section>

  <section class="card card--back" aria-label="Card back, contact details">
    <div class="card-finish" role="img" aria-label="Decorative blue and green pattern area"></div>
    <span class="mark-square"></span>
    <div class="wordmark"><span class="wordmark__main">Brightmoor</span></div>
    <p class="web">brightmoorsignal.com.au</p>
    <div class="contact">
      <h1 class="contact__name">Dorian Kestle</h1>
      <p class="contact__line">Phone: 38104472</p>
      <p class="contact__line">Fax: 38104473</p>
      <p class="contact__line">Email: dorian@kestleworks.au</p>
    </div>
  </section>

</body>
</html>
```